Business card for consulting firm

We need a double-sided business card for consulting firm, Vantorq. The card should be professional but also creative and visually interesting.

Target Market(s)

Engineering and technology; transport industries; safety critical / heavy industry.

Contact Information for Business Card

See attached file with details.

Font styles to use
Sans Serif

```html
<!DOCTYPE html>
<html lang="en">
<head>
<meta charset="UTF-8">
<title>Vantorq Business Card</title>
<link href="https://fonts.googleapis.com/css2?family=Work+Sans:wght@400;500;600;700&display=swap" rel="stylesheet">
<style>
  :root {
    --stage: #1b1b1c;
    --card-deep: #0a2133;
    --card-light: #16374b;
    --accent: #2bb4e6;
    --ink: #ffffff;
    --ink-soft: #dfe8ee;
  }
  * { margin: 0; padding: 0; box-sizing: border-box; }
  html, body {
    width: 1200px; height: 900px; overflow: hidden;
    background: var(--stage);
    font-family: "Work Sans", Arial, sans-serif;
    color: var(--ink);
  }
  .canvas {
    position: relative; width: 1200px; height: 900px;
    display: flex; flex-direction: column; align-items: center;
    justify-content: center; gap: 34px;
  }
  .card {
    position: relative; width: 700px; height: 400px;
    background: linear-gradient(135deg, var(--card-deep) 0%, var(--card-deep) 45%, var(--card-light) 100%);
    box-shadow: 0 10px 30px rgba(0,0,0,0.55);
    overflow: hidden;
  }
  .wordmark {
    font-weight: 600; letter-spacing: 0.08em; color: var(--ink);
    line-height: 1; white-space: nowrap;
  }
  .card-front .wordmark {
    position: absolute; top: 150px; left: 0; right: 0;
    text-align: center; font-size: 78px;
  }
  .card-front .web {
    position: absolute; bottom: 62px; left: 0; right: 0;
    text-align: center; font-size: 17px; letter-spacing: 0.12em;
    color: var(--ink-soft);
  }
  .accent { color: var(--accent); }
  .card-back .wordmark {
    position: absolute; top: 172px; left: 48px; font-size: 48px;
  }
  .divider {
    position: absolute; left: 338px; top: 112px; width: 2px; height: 186px;
    background: var(--accent);
  }
  .details { position: absolute; left: 372px; top: 108px; }
  .person-name {
    font-size: 29px; font-weight: 700; color: var(--accent); letter-spacing: 0.02em;
  }
  .credentials { font-size: 13px; margin-top: 6px; color: var(--ink-soft); letter-spacing: 0.03em; }
  .role { font-size: 18px; margin-top: 4px; letter-spacing: 0.06em; }
  .contacts { list-style: none; margin-top: 20px; }
  .contacts li {
    display: flex; align-items: center; gap: 14px;
    font-size: 17px; letter-spacing: 0.05em; line-height: 27px;
  }
  .contacts svg { width: 16px; height: 16px; flex: none; }
</style>
</head>
<body>
<main class="canvas">
  <section class="card card-front">
    <div class="wordmark">Vantorq</div>
    <div class="web">www.<span class="accent">vantorq</span>.com.au</div>
  </section>

  <section class="card card-back">
    <div class="wordmark">Vantorq</div>
    <div class="divider"></div>
    <div class="details">
      <div class="person-name">Helena Marwick</div>
      <div class="credentials">BA (Hons), M Psych Org, M Tech Mgt (HF)</div>
      <div class="role">Managing Director</div>
      <ul class="contacts">
        <li>
          <svg viewBox="0 0 16 16" aria-hidden="true"><path fill="var(--accent)" d="M3.6 1.5l2.2 2.6-1.3 1.6c.9 2 2.4 3.5 4.4 4.6l1.6-1.3 2.6 2.2-1.3 2.5C7 13.4 2.6 9 1.6 2.8z"/></svg>
          <span class="contact-text">+61 (0)400 555 018</span>
        </li>
        <li>
          <svg viewBox="0 0 16 16" aria-hidden="true"><rect x="1" y="3" width="14" height="10" fill="var(--accent)"/><path d="M1 3l7 6 7-6" fill="none" stroke="var(--card-deep)" stroke-width="1.3"/></svg>
          <span class="contact-text">hmarwick@vantorq.com.au</span>
        </li>
        <li>
          <svg viewBox="0 0 16 16" aria-hidden="true"><g fill="none" stroke="var(--accent)" stroke-width="1.2"><circle cx="8" cy="8" r="6.5"/><ellipse cx="8" cy="8" rx="3" ry="6.5"/><path d="M1.5 8h13M2.5 4.8h11M2.5 11.2h11"/></g></svg>
          <span class="contact-text">www.<span class="accent">vantorq</span>.global</span>
        </li>
        <li>
          <svg viewBox="0 0 16 16" aria-hidden="true"><g fill="none" stroke="var(--accent)" stroke-width="1.2"><circle cx="8" cy="8" r="6.5"/><ellipse cx="8" cy="8" rx="3" ry="6.5"/><path d="M1.5 8h13M2.5 4.8h11M2.5 11.2h11"/></g></svg>
          <span class="contact-text">www.vantorq.com.au</span>
        </li>
      </ul>
    </div>
  </section>
</main>
</body>
</html>
```